Bright Dune Series- Face & Body Oil Label

Hi,
I need a label design for a new brand- "Bright Dune Series". Modern and expensive looking. Any color scheme. Feel free to be creative! (I'm not set on the brand name above... I was also thinking maybe "LUXA" or "PuraGlow".
-Packaging: 4oz / 118mL clear glass "boston round" bottle with a white treatment pump. The product is an oil so it has a golden tint.
-Product: 4oz Biotin & Marula Face & Body Oil (note that the featured ingredients will change. Others will be "Rosehip & Vitamin E", "Lavender & Hemp Seed Oil", "Coconut Oil & Vitamin C"
-Label size: 5" x 2.5" rounded corners
-Main Highlight: "Moisturizing & Healing"
-Other Highlights:
-----non-greasy
-----all-natural
-----paraben-free
-----vegan
(feel free to use icon symbols)
-Ingredient deck attached
-Other info:
----made in Los Angeles, CA
----manufactured by Willowmark Blends LLC
----UPC
The main thing here is the logo and textures to the label. I can fill in / rearrange the info after.
Thank you,
Theo

```html
<!DOCTYPE html>
<html lang="en">
<head>
<meta charset="utf-8">
<title>PuraGlow Face &amp; Body Oil Label</title>
<link rel="stylesheet" href="https://fonts.googleapis.com/css2?family=Oswald:wght@400;500;600&display=swap">
<style>
  :root {
    --canvas: #e9e8e3;
    --label-white: #f4f4f2;
    --sand-light: #efe6dc;
    --sand-deep: #dcc5b2;
    --ice-blue: #6fa3b6;
    --ice-soft: #a9cbd8;
    --ink: #1c1c1e;
  }
  * { box-sizing: border-box; margin: 0; padding: 0; }
  html, body {
    width: 1200px;
    height: 1200px;
    overflow: hidden;
    background: var(--canvas);
  }
  .label {
    position: absolute;
    left: 255px;
    top: 105px;
    width: 690px;
    height: 990px;
    border-radius: 34px;
    overflow: hidden;
    background: var(--label-white);
    box-shadow: 0 2px 8px rgba(0,0,0,0.06);
    font-family: 'Oswald', sans-serif;
  }
  .label-top {
    height: 470px;
    display: flex;
    flex-direction: column;
    align-items: center;
    justify-content: center;
    gap: 34px;
  }
  .brand {
    display: flex;
    align-items: center;
    gap: 18px;
    color: var(--ice-blue);
    font-size: 76px;
    font-weight: 600;
    letter-spacing: 0.06em;
    text-transform: uppercase;
  }
  .brand-dot {
    width: 22px;
    height: 22px;
    border-radius: 50%;
    background: var(--ice-blue);
  }
  .highlight {
    color: var(--ice-blue);
    font-size: 26px;
    font-weight: 500;
    letter-spacing: 0.14em;
    text-transform: uppercase;
  }
  .divider {
    height: 14px;
    background: var(--ice-soft);
  }
  .label-bottom {
    height: 506px;
    background: linear-gradient(90deg, var(--sand-deep) 0%, var(--sand-light) 60%, var(--sand-light) 100%);
    display: flex;
    flex-direction: column;
    align-items: center;
    padding-top: 38px;
  }
  .product-type {
    color: var(--ice-blue);
    font-size: 92px;
    font-weight: 500;
    letter-spacing: 0.01em;
    line-height: 1.05;
  }
  .ingredients {
    margin-top: 22px;
    color: var(--ink);
    font-size: 62px;
    font-weight: 500;
    letter-spacing: 0.02em;
    line-height: 1;
  }
  .volume {
    margin-top: 52px;
    color: var(--ink);
    font-size: 30px;
    font-weight: 400;
    letter-spacing: 0.04em;
  }
  .maker {
    margin-top: 70px;
    color: var(--ink);
    font-size: 19px;
    font-weight: 500;
    line-height: 1.45;
    text-align: center;
    text-transform: uppercase;
  }
</style>
</head>
<body>
  <div class="label">
    <div class="label-top">
      <div class="brand"><span class="brand-dot"></span>PuraGlow</div>
      <div class="highlight">Moisturizing and Healing</div>
    </div>
    <div class="divider"></div>
    <div class="label-bottom">
      <div class="product-type">FACE &amp; BODY OIL</div>
      <div class="ingredients">BIOTIN &amp; MARULA</div>
      <div class="volume">4OZ / 118ML</div>
      <div class="maker">Made in Los Angeles, CA<br>Manufactured by Willowmark Blends LLC</div>
    </div>
  </div>
</body>
</html>
```